Craft oriented film company needs a Business Card design

Hi all,
We're a 2-man band film company in New Zealand called Kestrel Pictures. We're good honest blokes, who are very passionate about the craft of film making. I've attached our current logo which has a bit of a crafty/artisan feel that we like. Feel free to use it - or throw the baby out with the bathwater and start again..... you never know, you might inspire a complete brand re-work.

In any case, the vibe we want to give out is that we are solid, dependable and no bullshit - but without compromising creative excellence and being in the now. We like the 'Brooklyn' artisan style of work.

Preferably single sided.

We need the standard stuff:
Name, job title, cellphone, email address and physical address (this can be smaller if you like - street, suburb, city & zip, country [if you want])

Check out our website to learn more about us: kestrelpictures.example

Target Market(s)

Brand marketers and advertising agency creatives looking for video production.

Industry/Entity Type

Baby

Requirements
Should not have
• Nothing flashy or too 'futuristic', we want it to feel grounded and real. A limited colour palette is preferred.
We don't want any film reels or cameras or anything obvious like that.

```html
<!DOCTYPE html>
<html lang="en">
<head>
<meta charset="utf-8">
<title>Kestrel Pictures – Business Card</title>
<link rel="stylesheet" href="https://fonts.googleapis.com/css2?family=Jost:wght@400;500;600&display=swap">
<style>
  :root {
    --page-bg: #e6e6e4;
    --card-dark: #1c1c1c;
    --photo-light: #6a6a6a;
    --photo-mid: #3a3a3a;
    --band-white: #ffffff;
    --ink: #2b2b2b;
    --ink-soft: #7a7a7a;
    --accent: #3bb7c6;
    --address-grey: #b9b9b9;
  }
  * { margin: 0; padding: 0; box-sizing: border-box; }
  html, body {
    width: 1200px; height: 1000px; overflow: hidden;
    background: var(--page-bg);
    font-family: "Jost", "Futura", sans-serif;
  }
  .stage {
    width: 1200px; height: 1000px;
    display: flex; align-items: center; justify-content: center;
  }
  .business-card {
    position: relative;
    width: 900px; height: 514px;
    border-radius: 30px;
    overflow: hidden;
    background: var(--card-dark);
    box-shadow: 0 14px 40px rgba(0,0,0,0.25);
  }
  .staircase-photo {
    position: absolute; inset: 0;
    background: radial-gradient(circle at 40% 55%, var(--photo-light) 0%, var(--photo-mid) 35%, var(--card-dark) 75%);
  }
  .info-band {
    position: absolute; left: 0; right: 0; top: 100px; height: 170px;
    background: var(--band-white);
  }
  .brand-seal {
    position: absolute; left: 470px; top: 10px;
    width: 350px; height: 350px; border-radius: 50%;
    background: var(--band-white);
    display: flex; align-items: center; justify-content: center;
  }
  .brand-disc {
    width: 300px; height: 300px; border-radius: 50%;
    background: var(--card-dark);
    display: flex; align-items: center; justify-content: center;
    text-align: center;
  }
  .brand-name {
    color: var(--band-white);
    font-weight: 600; font-size: 40px; line-height: 1.1;
    letter-spacing: 1px; text-transform: uppercase;
  }
  .contact {
    position: absolute; left: 70px; top: 128px;
    color: var(--ink);
  }
  .contact .person-name { font-size: 32px; font-weight: 600; line-height: 1; }
  .contact .job-title { font-size: 17px; color: var(--ink-soft); margin-top: 4px; }
  .contact .phone { font-size: 20px; margin-top: 22px; }
  .contact .email { font-size: 20px; color: var(--accent); margin-top: 2px; }
  .footer-details {
    position: absolute; left: 70px; top: 370px;
  }
  .footer-details .website { font-size: 24px; color: var(--accent); letter-spacing: 0.5px; }
  .footer-details .address { font-size: 19px; color: var(--address-grey); margin-top: 14px; }
</style>
</head>
<body>
<main class="stage">
  <article class="business-card">
    <div class="staircase-photo" role="img" aria-label="Black and white photograph of a spiral staircase seen from above"></div>
    <div class="info-band"></div>
    <div class="brand-seal">
      <div class="brand-disc">
        <span class="brand-name">Kestrel<br>Pictures</span>
      </div>
    </div>
    <section class="contact">
      <p class="person-name">Dorian Pell</p>
      <p class="job-title">Accountant</p>
      <p class="phone">+64-21-55-0142</p>
      <p class="email">dorian@kestrelpictures.example</p>
    </section>
    <section class="footer-details">
      <p class="website">www.kestrelpictures.example</p>
      <p class="address">48 Harbour View Rd, Ponsonby, Auckland 1011</p>
    </section>
  </article>
</main>
</body>
</html>
```